Orvella Aid Fund - New Website Design

I need a site that looks like this http://renwick-gives-now.org for boat donations. So please replace the cars with boats.

```html
<!DOCTYPE html>
<html lang="en">
<head>
<meta charset="utf-8">
<title>Orvella Aid Fund – Donate Your Boat</title>
<link href="https://fonts.googleapis.com/css2?family=Open+Sans:wght@400;600;700&family=Roboto+Slab:wght@400&family=Kaushan+Script&display=swap" rel="stylesheet">
<style>
:root{
  --blue:#2aaed3;
  --blue-dark:#1f97b9;
  --yellow:#f0b92f;
  --orange:#ee6b1c;
  --ink:#2f3338;
  --muted:#7b8088;
  --pale:#f4f6fa;
  --line:#d9dde3;
  --white:#ffffff;
}
*{margin:0;padding:0;box-sizing:border-box}
html,body{width:1200px;height:2187px;overflow:hidden}
body{position:relative;background:var(--white);font-family:"Open Sans",Arial,sans-serif;color:var(--ink)}
.abs{position:absolute}
.slab{font-family:"Roboto Slab",Georgia,serif;font-weight:400}

/* header */
.brand{left:156px;top:40px;display:flex;align-items:center;gap:12px}
.brand-dot{width:40px;height:40px;border-radius:50%;background:var(--blue)}
.brand-name{font-size:28px;font-weight:600;color:var(--blue)}
.call{right:340px;top:46px;text-align:right}
.call strong{font-size:14px;font-weight:700;color:var(--ink)}
.call small{display:block;font-size:10px;color:var(--muted);margin-top:2px}
.call svg{vertical-align:-3px;margin:0 3px}
.btn{display:flex;align-items:center;justify-content:center;color:var(--white);font-family:"Kaushan Script",cursive;font-size:16px;border-bottom:2px solid rgba(0,0,0,.12)}
.btn-blue{background:var(--blue)}
.btn-yellow{background:var(--yellow)}
.donate-top{left:892px;top:45px;width:152px;height:38px}

/* nav */
.navbar{left:0;top:120px;width:1200px;height:48px;background:var(--blue)}
.nav-home{left:156px;top:120px;width:52px;height:48px;background:var(--yellow);display:flex;align-items:center;justify-content:center}
.nav-links{left:236px;top:120px;height:48px;display:flex;align-items:center;gap:22px;color:var(--white);font-size:12px;font-weight:600}
.nav-links i{font-style:normal;opacity:.8}

/* hero */
.hero{left:0;top:168px;width:1200px;height:302px;background:linear-gradient(90deg,#c4644f 0%,#d27a63 35%,#e3c9bf 52%,#cf6e58 75%,#c85d49 100%)}
.hero-title{left:156px;top:266px;font-size:29px;color:var(--white);line-height:35px}
.hero-sub{left:156px;top:350px;font-size:12px;color:var(--white)}

/* sections */
.welcome-bg{left:0;top:470px;width:1200px;height:354px;background:var(--pale)}

/* form */
.form-card{left:688px;top:112px;width:356px;height:406px}
.form-head{left:688px;top:120px;width:356px;height:55px;background:var(--yellow);text-align:center;padding-top:8px}
.form-head h2{font-size:18px;font-weight:400;color:var(--ink);line-height:22px}
.form-head p{font-size:10px;color:var(--ink)}
.field{position:absolute;height:32px;border:1px solid var(--line);background:var(--white);font-size:10px;color:#9aa0a8;padding:0 14px;display:flex;align-items:center;justify-content:space-between}
.submit{left:783px;top:432px;width:160px;height:38px}

.dots{left:156px;top:509px;display:flex;gap:6px}
.dots span{width:8px;height:8px;border-radius:50%;border:1px solid var(--blue)}
.dots span.on{background:var(--blue)}

.section-title{width:1200px;left:0;text-align:center;font-size:30px;color:var(--ink)}
.section-title em{font-style:normal;color:var(--yellow);font-family:"Kaushan Script",cursive}
.divider{left:360px;width:480px;height:12px}
.welcome-text{left:240px;top:640px;width:720px;text-align:center;font-size:12px;line-height:18px;color:#555a61}
.our-story{left:535px;top:720px;width:128px;height:38px}

.why-note{left:0;top:1326px;width:1200px;text-align:center;font-size:14px;color:var(--ink)}
.donate-mid{left:523px;top:1357px;width:152px;height:38px}

/* faq */
.faq-bg{left:0;top:1458px;width:1200px;height:558px;background:linear-gradient(120deg,#6c7f8a 0%,#8fa6ae 30%,#5f8ea2 55%,#8a9aa0 80%,#6f7f86 100%)}
.faq-title{color:var(--white)}
.faq-list{left:232px;top:1612px;width:735px;list-style:none}
.faq-list li{height:41px;margin-bottom:8.6px;background:rgba(42,174,211,.78);color:var(--white);font-size:14px;display:flex;align-items:center;justify-content:space-between;padding:0 22px}
.faq-list li b{font-size:18px;font-weight:700}

/* footer */
.footer{left:0;top:2016px;width:1200px;height:171px;background:var(--pale)}
.foot-call{left:156px;top:2076px;font-size:13px;color:var(--ink)}
.foot-call span{color:var(--yellow)}
.foot-copy{left:156px;top:2110px;font-size:11px;color:var(--muted)}
.socials{left:906px;top:2079px;display:flex;gap:9px}
.socials span{width:20px;height:20px;border-radius:50%;background:#cfd4da}
.socials span.on{background:var(--blue)}
.foot-links{right:156px;top:2110px;font-size:12px;color:var(--muted);display:flex;gap:10px}
</style>
</head>
<body>

<!-- header -->
<div class="abs brand"><span class="brand-dot"></span><span class="brand-name">Orvella Aid Fund</span></div>
<div class="abs call">
  <strong>Call Us:<svg width="14" height="14" viewBox="0 0 24 24"><circle cx="12" cy="12" r="11" fill="none" stroke="#f0b92f" stroke-width="2"/><path d="M8 6l2 0 1 3-1.5 1.2a7 7 0 0 0 4.3 4.3L15 13l3 1v2a2 2 0 0 1-2 2A10 10 0 0 1 6 8a2 2 0 0 1 2-2z" fill="#f0b92f"/></svg>1-800-555-0148</strong>
  <small>Live Operators Available - 7 Days A Week</small>
</div>
<div class="abs btn btn-blue donate-top">Donate Now</div>

<!-- nav -->
<div class="abs navbar"></div>
<div class="abs nav-home"><svg width="16" height="14" viewBox="0 0 16 14"><path d="M8 0L0 7h2v7h4V9h4v5h4V7h2z" fill="#fff"/></svg></div>
<nav class="abs nav-links"><span>Our Story</span><i>|</i><span>Whay Us</span><i>|</i><span>Contact Us</span></nav>

<!-- hero -->
<div class="abs hero" role="img" aria-label="Photo of a smiling child wearing a pink head scarf"></div>
<div class="abs hero-title">Donate Boat to<br>Charity!</div>
<div class="abs hero-sub">Your boat can make a difference!</div>

<!-- welcome background (sits under the form card) -->
<div class="abs welcome-bg"></div>

<!-- pickup form -->
<svg class="abs form-card" viewBox="0 0 356 406" style="filter:drop-shadow(0 4px 8px rgba(0,0,0,.12))">
  <path d="M0 0H356V358L178 406L0 358Z" fill="#fff"/>
  <rect width="356" height="8" fill="#ee6b1c"/>
</svg>
<div class="abs form-head"><h2>Donate to Orvella Aid Fund</h2><p>Donation PickUp Form</p></div>
<div class="field" style="left:720px;top:200px;width:292px">Name</div>
<div class="field" style="left:720px;top:244px;width:140px">Phone</div>
<div class="field" style="left:872px;top:244px;width:140px">Zip Code <span>&#8964;</span></div>
<div class="field" style="left:720px;top:288px;width:292px">Email</div>
<div class="field" style="left:720px;top:332px;width:292px">Model of Boat</div>
<div class="field" style="left:720px;top:376px;width:140px">Year <span>&#8964;</span></div>
<div class="field" style="left:872px;top:376px;width:140px">Make <span>&#8964;</span></div>
<div class="abs btn btn-blue submit">Submit Application</div>

<!-- welcome -->
<div class="abs dots"><span></span><span class="on"></span><span></span><span></span></div>
<h1 class="abs section-title slab" style="top:552px">Welcome to Orvella Aid Fund</h1>
<svg class="abs divider" style="top:606px" viewBox="0 0 480 12"><line x1="0" y1="6" x2="480" y2="6" stroke="#d9dde3"/><circle cx="240" cy="5" r="3.5" fill="#fff" stroke="#b8bec6"/></svg>
<p class="abs welcome-text">Orvella Aid Fund Foundation's mission is to improve, empower and to bring joy to the lives of children and their families affected by cancer. Orvella Aid Fund adapts its support to fit each child's needs; from education to assistance with treatment, recovery and family support.</p>
<div class="abs btn btn-yellow our-story">Our Story</div>

<!-- why donate -->
<h2 class="abs section-title slab" style="top:888px">Why Donate Tour <em>Boat</em> To Us</h2>
<svg class="abs divider" style="top:942px" viewBox="0 0 480 12"><line x1="0" y1="6" x2="480" y2="6" stroke="#d9dde3"/><circle cx="240" cy="5" r="3.5" fill="#fff" stroke="#b8bec6"/></svg>
<svg class="abs" style="left:0;top:960px" width="1200" height="350" viewBox="0 960 1200 350">
  <path d="M156 1289H309V1206A291 200 0 0 1 891 1206V1289H1044" fill="none" stroke="#f0b92f" stroke-width="1.5"/>
  <path d="M412 1289A188 174 0 0 1 588 1116L600 1103L612 1116A188 174 0 0 1 788 1289Z" fill="#f0b92f"/>
  <path d="M600 1062c-18-18-32-28-32-48a32 32 0 0 1 64 0c0 20-14 30-32 48z" fill="#f0b92f"/>
  <path d="M586 1010h28l-4 10h-20z M590 1000h20v8h-20z M584 1024c5 3 10 3 16 0c6 3 11 3 16 0" fill="none" stroke="#fff" stroke-width="2.5"/>
  <circle cx="350" cy="1152" r="32" fill="#fff" stroke="#f0b92f" stroke-width="1.5"/>
  <path d="M336 1162h18v-8h8l4 8h2M334 1166h34M340 1150l16-12M356 1138v10" fill="none" stroke="#f0b92f" stroke-width="2.5"/>
  <circle cx="849" cy="1152" r="32" fill="#fff" stroke="#f0b92f" stroke-width="1.5"/>
  <path d="M836 1168h22M842 1148l10-10 8 8-10 10zM847 1153l-10 10" fill="none" stroke="#f0b92f" stroke-width="3"/>
  <rect x="207" y="1277" width="24" height="24" transform="rotate(45 219 1289)" fill="#f4f6fa"/>
  <path d="M222 1283l-6 6 6 6" fill="none" stroke="#2aaed3" stroke-width="2"/>
  <rect x="964" y="1275" width="28" height="28" transform="rotate(45 978 1289)" fill="#2aaed3"/>
  <path d="M975 1283l6 6-6 6" fill="none" stroke="#fff" stroke-width="2"/>
  <text x="600" y="1207" text-anchor="middle" fill="#fff" font-family="Open Sans, sans-serif" font-size="18">We Accept</text>
  <text x="600" y="1235" text-anchor="middle" fill="#fff" font-family="Open Sans, sans-serif" font-size="18">All Type of Boats</text>
</svg>
<p class="abs why-note">Your boat can make a difference!</p>
<div class="abs btn btn-blue donate-mid">Donate Now</div>

<!-- faq -->
<div class="abs faq-bg" role="img" aria-label="Photo of a family embracing outdoors, with a soft blue overlay"></div>
<h2 class="abs section-title slab faq-title" style="top:1519px">Frequently <em>Asked</em> Questions</h2>
<svg class="abs divider" style="top:1573px" viewBox="0 0 480 12"><line x1="0" y1="6" x2="480" y2="6" stroke="rgba(255,255,255,.7)"/><circle cx="240" cy="5" r="3.5" fill="none" stroke="#fff"/></svg>
<ul class="abs faq-list">
  <li><span>01.&nbsp; What types of vehicles can be donated?</span><b>+</b></li>
  <li><span>02.&nbsp; What paperwork do I need to donate my vehicle?</span><b>+</b></li>
  <li><span>03.&nbsp; Is my donated vehicle tax-deductible?</span><b>+</b></li>
  <li><span>04.&nbsp; What if the vehicle is not registered in my name?</span><b>+</b></li>
  <li><span>05.&nbsp; How much will I receive as a tax deduction for my vehicle?</span><b>+</b></li>
  <li><span>06.&nbsp; When will I receive my tax receipt?</span><b>+</b></li>
  <li><span>07.&nbsp; How do I schedule a pick up?</span><b>+</b></li>
</ul>

<!-- footer -->
<div class="abs footer"></div>
<p class="abs foot-call">Call Today to Donate! <span>1-888-555-0192</span> or <span>Email Us</span></p>
<p class="abs foot-copy">© 2017 Orvella Aid Fund . All Rights Reserved.</p>
<div class="abs socials"><span></span><span></span><span class="on"></span><span></span><span></span></div>
<nav class="abs foot-links"><span>Home</span><span>|</span><span>About Us</span><span>|</span><span>Contact Us</span></nav>

</body>
</html>
```